Postcard for septic company
K Dorsey Wastewater Services LLC.
PUMP THAT SEPTIC!!!
Please go to my website for info about my company. kdwastepro.com i also have alot of info on the companys chatterbook page. chatterbook.net/kdwastepro.
When making the postcard please have a $10.00 off coupon on it.
We are a full service Septic company. We offer septic tank and cesspool pumping and septic system repairs. You can use my chatterbook cover on the post card. Maybe have it say. "When was the last time you had your septic system serviced?? If you cant remember its been to long!! I will upload my logo and cover image on my chatterbook.
Utilities
Homeowners and business
- include indicia and address bar on one half of the postcard
- provide design in both sizes: 8.5 x 11 and 6.5 x 9
- double sided design
NOTE FOLLOWING:
- These postcards are going to be for the NPDS Each Street Bulk Post program and do not need a place for addresses. The only addressing/postage required are the Local Postal Customer box and the indicia.
Please go to NPDS website for more info.
logo
chatterbook cover

```html
<!DOCTYPE html>
<html lang="en">
<head>
<meta charset="utf-8">
<title>K Dorsey Wastewater Services – Postcards</title>
<link rel="stylesheet" href="https://fonts.googleapis.com/css2?family=Open+Sans:ital,wght@0,400;0,600;0,700;1,400;1,600&display=swap">
<style>
  :root{
    --navy:#1c2244;
    --navy-2:#2a3163;
    --blue:#2b5fb3;
    --bright:#3a78d6;
    --green:#4f7a2a;
    --green-dark:#3a5c1d;
    --grey:#dfe2e8;
    --grey-2:#b9bfcb;
    --page:#eceef2;
    --white:#ffffff;
    --ink:#2a2f45;
  }
  *{box-sizing:border-box;margin:0;padding:0}
  html,body{width:1200px;height:1060px;overflow:hidden}
  body{background:var(--page);font-family:"Open Sans",Arial,sans-serif;position:relative;color:var(--ink)}

  .card{position:absolute;overflow:hidden;box-shadow:0 4px 14px rgba(0,0,0,.25);--u:1px}
  .card--small{--u:0.865px}
  .front-small{left:63px;top:57px;width:495px;height:400px}
  .front-large{left:586px;top:57px;width:572px;height:472px}
  .back-small{left:63px;top:543px;width:486px;height:443px}
  .back-large{left:586px;top:543px;width:572px;height:486px}

  /* ---------- front ---------- */
  .front{background:var(--navy)}
  .front__header{position:absolute;left:0;top:0;width:100%;height:20%;background:linear-gradient(180deg,var(--navy-2),var(--navy))}
  .brand{position:absolute;background:var(--white);display:flex;align-items:center;justify-content:center;gap:calc(var(--u)*7)}
  .brand__mark{width:calc(var(--u)*14);height:calc(var(--u)*14);background:var(--blue)}
  .brand__name{font-weight:700;color:var(--navy);font-size:calc(var(--u)*19);letter-spacing:.04em}
  .front .brand{left:calc(var(--u)*22);top:14%;width:calc(var(--u)*130);height:76%;border-radius:calc(var(--u)*3)}
  .call{position:absolute;right:calc(var(--u)*26);top:12%;text-align:right;color:var(--white)}
  .call__label{font-style:italic;font-weight:600;font-size:calc(var(--u)*17)}
  .call__number{font-weight:700;font-size:calc(var(--u)*28);line-height:1.1}
  .front__photo{position:absolute;left:0;top:20%;width:100%;height:43.5%;
    background:linear-gradient(180deg,#9fb88a 0%,#6f8f5a 35%,#d9dde0 55%,#8a9480 80%,#5d6b4c 100%)}
  .front__message{position:absolute;left:0;top:63.5%;width:100%;height:12.5%;
    background:linear-gradient(180deg,var(--navy-2),var(--navy));color:var(--white);text-align:center;
    display:flex;flex-direction:column;justify-content:center;font-size:calc(var(--u)*14.5);line-height:1.35}
  .front__footer{position:absolute;left:0;top:76%;width:100%;height:24%;background:linear-gradient(180deg,var(--grey),var(--grey-2))}
  .contact{position:absolute;left:0;top:0;width:31%;height:100%;background:var(--navy);color:var(--white);
    font-size:calc(var(--u)*10.5);line-height:1.5;padding:calc(var(--u)*20) 0 0 calc(var(--u)*16)}
  .contact__web{font-weight:700}
  .social{position:absolute;left:34%;top:32%;display:flex;align-items:center;gap:calc(var(--u)*5);
    font-size:calc(var(--u)*10);color:var(--ink);line-height:1.2}
  .social__mark{width:calc(var(--u)*20);height:calc(var(--u)*20);background:var(--blue)}
  .payments{position:absolute;left:58%;top:36%;display:flex;gap:calc(var(--u)*6)}
  .payments span{width:calc(var(--u)*30);height:calc(var(--u)*19);border-radius:calc(var(--u)*2);background:var(--white);border:1px solid #9aa2b3}
  .coupon{position:absolute;right:calc(var(--u)*30);top:75%;width:calc(var(--u)*80);height:calc(var(--u)*80);border-radius:50%;
    background:radial-gradient(circle at 40% 35%,#6c9a3c,var(--green-dark));color:var(--white);font-weight:700;
    display:flex;flex-direction:column;align-items:center;justify-content:center;line-height:1.05;
    box-shadow:0 2px 6px rgba(0,0,0,.35)}
  .coupon__amount{font-size:calc(var(--u)*18)}
  .coupon__word{font-size:calc(var(--u)*16)}

  /* ---------- back ---------- */
  .back{background:var(--white)}
  .back .brand{left:calc(var(--u)*18);top:calc(var(--u)*18);width:calc(var(--u)*130);height:calc(var(--u)*56);justify-content:flex-start}
  .address{position:absolute;left:calc(var(--u)*20);top:calc(var(--u)*84);font-size:calc(var(--u)*10);line-height:1.45;color:var(--ink)}
  .slogan{position:absolute;left:0;top:calc(var(--u)*124);width:62%;height:calc(var(--u)*22);
    background:linear-gradient(90deg,var(--navy) 0%,var(--blue) 55%,rgba(43,95,179,0) 100%);
    color:var(--white);font-weight:700;font-size:calc(var(--u)*10.5);display:flex;align-items:center;padding-left:calc(var(--u)*20)}
  .services{position:absolute;left:calc(var(--u)*20);top:calc(var(--u)*160);color:var(--blue);font-size:calc(var(--u)*10.5)}
  .services__title{font-weight:600;margin-bottom:calc(var(--u)*6)}
  .services ul{list-style:none;padding-left:calc(var(--u)*14)}
  .services li{position:relative;line-height:1.75}
  .services li::before{content:"";position:absolute;left:calc(var(--u)*-12);top:.62em;width:calc(var(--u)*5);height:calc(var(--u)*5);border-radius:50%;background:var(--bright)}
  .indicia{position:absolute;right:calc(var(--u)*20);top:calc(var(--u)*14);width:calc(var(--u)*74);height:calc(var(--u)*70);
    border:1px solid var(--ink);font-size:calc(var(--u)*7.5);line-height:1.3;text-align:center;padding-top:calc(var(--u)*8);font-weight:600}
  .recipient{position:absolute;left:57%;top:calc(var(--u)*196);width:calc(var(--u)*215);height:calc(var(--u)*48);
    border:1px solid var(--ink);font-size:calc(var(--u)*10);line-height:1.45;padding:calc(var(--u)*8) 0 0 calc(var(--u)*10)}
  .serving{position:absolute;left:calc(var(--u)*20);bottom:calc(var(--u)*64);font-size:calc(var(--u)*10);color:var(--ink)}
  .back__footer{position:absolute;left:0;bottom:0;width:100%;height:calc(var(--u)*44);background:var(--navy);color:var(--white);
    display:flex;align-items:center;justify-content:space-between;padding:0 calc(var(--u)*20);font-size:calc(var(--u)*10)}
  .back-small .serving{bottom:calc(var(--u)*62)}
</style>
</head>
<body>

<section class="card card--small front front-small">
  <div class="front__header">
    <div class="brand"><span class="brand__mark"></span><span class="brand__name">DORSEY</span></div>
    <div class="call"><div class="call__label">Call Us Today</div><div class="call__number">555-010-4172</div></div>
  </div>
  <div class="front__photo" role="img" aria-label="Photo of the company's septic pumping trucks parked on a lawn"></div>
  <div class="front__message"><p>When was the last time you had your septic system serviced?</p><p>If you cant remember its been to long!!</p></div>
  <div class="front__footer">
    <div class="contact"><div class="contact__web">www.kdwastepro.com</div><div>Phone: 555-010-4172</div><div>Fax: 555-010-4171</div></div>
    <div class="social"><span class="social__mark"></span><span>Find us on<br>chatterbook</span></div>
    <div class="payments"><span></span><span></span></div>
  </div>
  <div class="coupon"><span class="coupon__amount">$10.00</span><span class="coupon__word">OFF</span></div>
</section>

<section class="card front front-large">
  <div class="front__header">
    <div class="brand"><span class="brand__mark"></span><span class="brand__name">DORSEY</span></div>
    <div class="call"><div class="call__label">Call Us Today</div><div class="call__number">555-010-4172</div></div>
  </div>
  <div class="front__photo" role="img" aria-label="Photo of the company's septic pumping trucks parked on a lawn"></div>
  <div class="front__message"><p>When was the last time you had your septic system serviced?</p><p>If you cant remember its been to long!!</p></div>
  <div class="front__footer">
    <div class="contact"><div class="contact__web">www.kdwastepro.com</div><div>Phone: 555-010-4172</div><div>Fax: 555-010-4171</div></div>
    <div class="social"><span class="social__mark"></span><span>Find us on<br>chatterbook</span></div>
    <div class="payments"><span></span><span></span></div>
  </div>
  <div class="coupon"><span class="coupon__amount">$10.00</span><span class="coupon__word">OFF</span></div>
</section>

<section class="card card--small back back-small">
  <div class="brand"><span class="brand__mark"></span><span class="brand__name">DORSEY</span></div>
  <div class="address"><div>118 Meadow Lane</div><div>Birch Hollow PA 19000</div></div>
  <div class="slogan">PUMP THAT SEPTIC!</div>
  <div class="services">
    <div class="services__title">Our Services Include:</div>
    <ul>
      <li>Septic Tank and Cesspool Pumping</li>
      <li>Holding Tank Pumping</li>
      <li>Grease Trap Cleaning</li>
      <li>24/7 Emergency Services</li>
      <li>Septic Repairs</li>
    </ul>
  </div>
  <div class="indicia">PRSRT STD<br>ECRWSS<br>NPDS POSTAGE<br>PAID<br>ESBP RETAIL</div>
  <div class="recipient"><div>Local</div><div>Postal Customer</div></div>
  <p class="serving">Serving all of Delaware County and Southern Chester County.</p>
  <div class="back__footer"><span>www.kdwastepro.com</span><span>Phone: 555-010-4172</span><span>Fax: 555-010-4171</span></div>
</section>

<section class="card back back-large">
  <div class="brand"><span class="brand__mark"></span><span class="brand__name">DORSEY</span></div>
  <div class="address"><div>118 Meadow Lane</div><div>Birch Hollow PA 19000</div></div>
  <div class="slogan">PUMP THAT SEPTIC!</div>
  <div class="services">
    <div class="services__title">Our Services Include:</div>
    <ul>
      <li>Septic Tank and Cesspool Pumping</li>
      <li>Holding Tank Pumping</li>
      <li>Grease Trap Cleaning</li>
      <li>24/7 Emergency Services</li>
      <li>Septic Repairs</li>
    </ul>
  </div>
  <div class="indicia">PRSRT STD<br>ECRWSS<br>NPDS POSTAGE<br>PAID<br>ESBP RETAIL</div>
  <div class="recipient"><div>Local</div><div>Postal Customer</div></div>
  <p class="serving">Serving all of Delaware County and Southern Chester County.</p>
  <div class="back__footer"><span>www.kdwastepro.com</span><span>Phone: 555-010-4172</span><span>Fax: 555-010-4171</span></div>
</section>

</body>
</html>
```